We need an attractive business card design that is modern and inviting. We like the blue and yellow (or gold) colors that are displayed with the logo. The business should communicate trust, experience, and integrity.

Target Market(s)

Residential and Commercial

Industry/Entity Type

Business

Contact Information for Business Card

Recessed Lighting
LED Retro Fit
Sign Repair
Alarms and Cameras
Mobile Home Services
24hr service calls

Font styles to use
Serif
Sans Serif

Colors
3176b5
0455a3
fece3e
fbee3e

Requirements
Must have
• Brannick Electric
• Owner: Marcus Brannick
• Licensed and Insured
• TECL #58731
Nice to have
• Exquisite Detail!!
• Over 20 years of experience
Should not have
• Nothing boring or traditional!!!

```html
<!DOCTYPE html>
<html lang="en">
<head>
<meta charset="utf-8">
<title>Brannick Electric – Business Card</title>
<link rel="stylesheet" href="https://fonts.googleapis.com/css2?family=Open+Sans:wght@400;600;700&display=swap">
<style>
  :root {
    --canvas: #4a4a4a;
    --blue: #0455a3;
    --blue-light: #3176b5;
    --yellow: #fbee3e;
    --white: #ffffff;
    --ink-blue: #0a3f80;
  }
  * { margin: 0; padding: 0; box-sizing: border-box; }
  html, body { width: 1200px; height: 1000px; overflow: hidden; }
  body {
    background: var(--canvas);
    font-family: "Open Sans", Arial, sans-serif;
    position: relative;
  }
  .card {
    position: absolute;
    border-radius: 16px;
    overflow: hidden;
  }

  /* Front */
  .card-front {
    left: 111px; top: 105px; width: 638px; height: 352px;
    background: var(--blue);
  }
  .front-ring {
    position: absolute; left: 400px; top: 45px;
  }
  .front-mark {
    position: absolute; left: 145px; top: 27px;
    width: 78px; height: 78px; border-radius: 50%;
    border: 7px solid var(--white);
  }
  .front-name {
    position: absolute; left: 32px; top: 104px;
    font-size: 29px; font-weight: 700; color: var(--white);
    letter-spacing: 0; white-space: nowrap;
  }
  .owner {
    position: absolute; left: 32px; top: 188px;
    font-size: 22px; font-weight: 700; color: var(--white); letter-spacing: 1px;
  }
  .owner-rule {
    position: absolute; left: 32px; right: 0; top: 220px;
    height: 2px; background: var(--yellow);
  }
  .address {
    position: absolute; left: 32px; top: 230px;
    font-size: 14px; line-height: 18px; color: var(--yellow); letter-spacing: 0.4px;
  }
  .contact-line {
    position: absolute; left: 32px; display: flex; align-items: center; gap: 7px;
    font-size: 16px; color: var(--yellow); letter-spacing: 0.3px;
  }
  .contact-phone { top: 270px; }
  .contact-email { top: 293px; }
  .license {
    position: absolute; right: 16px; top: 294px;
    font-size: 14px; font-weight: 600; color: var(--white); letter-spacing: 0.4px;
  }
  .web-band {
    position: absolute; left: 0; right: 0; bottom: 0; height: 32px;
    background: var(--yellow); color: var(--ink-blue);
    font-size: 15px; letter-spacing: 2px; text-align: center; line-height: 30px;
  }

  /* Back */
  .card-back {
    left: 475px; top: 543px; width: 646px; height: 352px;
    background: radial-gradient(ellipse at 50% 45%, var(--blue-light) 0%, var(--blue) 70%);
  }
  .side-bar {
    position: absolute; top: 27px; width: 14px; height: 298px; background: var(--yellow);
  }
  .side-bar-left { left: 0; border-radius: 0 6px 6px 0; }
  .side-bar-right { right: 0; border-radius: 6px 0 0 6px; }
  .back-mark {
    position: absolute; left: 278px; top: 40px;
    width: 108px; height: 108px; border-radius: 50%;
    border: 9px solid var(--white);
  }
  .back-name {
    position: absolute; left: 0; right: 0; top: 147px; text-align: center;
    font-size: 41px; font-weight: 700; color: var(--white); letter-spacing: 0;
  }
  .services {
    position: absolute; left: 0; right: 0; top: 254px; text-align: center;
    font-size: 15px; font-weight: 600; color: var(--white); line-height: 22px; letter-spacing: 0.3px;
  }
  .dot {
    display: inline-block; width: 7px; height: 7px; border-radius: 50%;
    background: var(--yellow); margin: 0 4px; vertical-align: 2px;
  }
  .experience {
    position: absolute; left: 0; right: 0; top: 312px;
    display: flex; justify-content: center; align-items: center; gap: 8px;
    font-size: 15px; font-weight: 600; color: var(--white); letter-spacing: 0.4px;
  }
  .experience-rule { width: 20px; height: 2px; background: var(--yellow); }
</style>
</head>
<body>
  <section class="card card-front" aria-label="Business card front">
    <svg class="front-ring" width="230" height="230" viewBox="0 0 230 230" aria-hidden="true">
      <circle cx="115" cy="115" r="106" fill="none" stroke="rgba(255,255,255,0.22)" stroke-width="14"/>
    </svg>
    <div class="front-mark" aria-hidden="true"></div>
    <h1 class="front-name">BRANNICK ELECTRIC</h1>
    <p class="owner">Marcus Brannick</p>
    <div class="owner-rule"></div>
    <p class="address">1111 Harlow Lane<br>Cedar Hollow, TX</p>
    <p class="contact-line contact-phone">
      <svg width="15" height="15" viewBox="0 0 16 16" aria-hidden="true">
        <circle cx="8" cy="8" r="7" fill="none" stroke="#fff" stroke-width="1.4"/>
        <path d="M5.5 4.5c.4-.3.8-.2 1 .2l.6 1.2c.1.3 0 .6-.2.8l-.4.3c.4.9 1.1 1.6 2 2l.3-.4c.2-.2.5-.3.8-.2l1.2.6c.4.2.5.6.2 1-.5.7-1.2.9-2 .6-1.9-.7-3.3-2.1-4-4-.3-.8-.1-1.5.5-2.1z" fill="#fff"/>
      </svg>
      936-555-0147
    </p>
    <p class="contact-line contact-email">
      <svg width="15" height="11" viewBox="0 0 15 11" aria-hidden="true">
        <rect x="0" y="0" width="15" height="11" fill="#fff"/>
        <path d="M0.5 0.8 L7.5 6 L14.5 0.8" fill="none" stroke="#0455a3" stroke-width="1.3"/>
      </svg>
      info@yourweb.com
    </p>
    <p class="license">Licensed and Insured TECL #58731</p>
    <div class="web-band">www.yourweb.com</div>
  </section>

  <section class="card card-back" aria-label="Business card back">
    <div class="side-bar side-bar-left"></div>
    <div class="side-bar side-bar-right"></div>
    <div class="back-mark" aria-hidden="true"></div>
    <h2 class="back-name">BRANNICK ELECTRIC</h2>
    <p class="services">
      Residential and Commercial<span class="dot"></span>Recessed Lighting<span class="dot"></span>LED Retro Fit<span class="dot"></span>Sign Repair<br>
      Alarms and Cameras<span class="dot"></span>Mobile Home Services<span class="dot"></span>24hr service calls
    </p>
    <p class="experience">
      <span class="experience-rule"></span>Over 20 years of Experience<span class="experience-rule"></span>
    </p>
  </section>
</body>
</html>
```